Cindermoor Larder Logo/Label Design

I am designing a blueberry label that will be placed on clam shells when the fruit is packed. The label will the company name "The Cindermoor Larder". It will also list Blueberries/Bleuets (Blueberries in French). It small print it would say Dist. By/Par The Cindermoor Larder, Quillby, SC 39724 USA. It would also list the package size. 1 US Dry Pint/1 Chopine Seche US 551 ml. I have provided some sample labels that other marketers use.

```html
<!DOCTYPE html>
<html lang="en">
<head>
<meta charset="utf-8">
<title>The Cindermoor Larder – Blueberries Label</title>
<link href="https://fonts.googleapis.com/css2?family=Fredoka:wght@600&family=Poppins:wght@600;700&display=swap" rel="stylesheet">
<style>
  :root {
    --navy: #2e2b6b;
    --band: #474889;
    --paper: #e6e4f1;
    --lilac: #8a80c0;
    --white: #ffffff;
    --leaf: #6f9e3c;
    --berry: #5b78b0;
  }
  html, body {
    margin: 0;
    padding: 0;
    width: 1200px;
    height: 840px;
    overflow: hidden;
    background: var(--white);
  }
  .canvas {
    position: relative;
    width: 1200px;
    height: 840px;
  }
  .label-art {
    position: absolute;
    inset: 0;
  }
  .brand {
    position: absolute;
    left: 0;
    width: 1200px;
    text-align: center;
    font-family: "Fredoka", sans-serif;
    font-weight: 600;
    color: var(--band);
    line-height: 1;
  }
  .brand-the { top: 158px; font-size: 28px; letter-spacing: 1px; }
  .brand-name { top: 188px; font-size: 60px; letter-spacing: 1px; }
  .brand-sub { top: 248px; font-size: 30px; letter-spacing: 2px; }
  .brand-rule {
    position: absolute;
    top: 259px;
    width: 54px;
    height: 3px;
    border-radius: 2px;
    background: var(--band);
  }
  .brand-rule-left { left: 466px; }
  .brand-rule-right { left: 680px; }
  .product {
    position: absolute;
    left: 0;
    width: 1200px;
    text-align: center;
    font-family: "Poppins", sans-serif;
    font-weight: 700;
    color: var(--white);
    line-height: 1;
    letter-spacing: 3px;
    font-size: 66px;
  }
  .product-en { top: 338px; }
  .product-fr { top: 411px; }
  .size {
    position: absolute;
    left: 0;
    width: 1200px;
    text-align: center;
    font-family: "Poppins", sans-serif;
    font-weight: 600;
    color: var(--lilac);
    font-size: 26px;
    line-height: 1;
  }
  .size-us { top: 536px; }
  .size-fr { top: 572px; }
  .divider {
    position: absolute;
    left: 560px;
    top: 626px;
    width: 80px;
    height: 4px;
    border-radius: 2px;
    background: var(--band);
  }
  .dist-text {
    font-family: "Poppins", sans-serif;
    font-weight: 600;
    font-size: 13.5px;
    letter-spacing: 1.6px;
    fill: var(--band);
  }
</style>
</head>
<body>
<div class="canvas">
  <svg class="label-art" width="1200" height="840" viewBox="0 0 1200 840">
    <defs>
      <path id="label-shape" d="M275,188 C380,186 430,165 480,140 C530,118 560,107 601,107 C642,107 672,118 722,140 C772,165 822,186 928,188 C930,235 960,264 1004,264 L1004,571 C960,571 930,600 928,645 C822,647 772,668 722,692 C672,716 642,728 601,728 C560,728 530,716 480,692 C430,668 380,647 275,645 C273,600 243,571 198,571 L198,264 C243,264 273,235 275,188 Z"/>
      <clipPath id="label-clip"><use href="#label-shape"/></clipPath>
      <linearGradient id="sprig-fill" x1="0" y1="0" x2="0" y2="1">
        <stop offset="0" stop-color="var(--leaf)"/>
        <stop offset="0.45" stop-color="var(--leaf)"/>
        <stop offset="0.6" stop-color="var(--berry)"/>
        <stop offset="1" stop-color="var(--berry)"/>
      </linearGradient>
      <path id="dist-arc" d="M365,612 C460,660 530,700 602,703 C680,700 750,660 852,608"/>
    </defs>

    <use href="#label-shape" fill="var(--paper)"/>
    <rect class="title-band" x="198" y="310" width="806" height="194" fill="var(--band)" clip-path="url(#label-clip)"/>

    <g clip-path="url(#label-clip)">
      <rect role="img" aria-label="Engraved illustration of blueberry leaves and a cluster of blueberries" x="200" y="252" width="156" height="296" rx="40" fill="url(#sprig-fill)"/>
      <rect role="img" aria-label="Engraved illustration of blueberry leaves and a cluster of blueberries" x="844" y="250" width="158" height="298" rx="40" fill="url(#sprig-fill)"/>
    </g>

    <use href="#label-shape" fill="none" stroke="var(--navy)" stroke-width="4"/>
    <use href="#label-shape" fill="none" stroke="var(--navy)" stroke-width="1.6" transform="translate(601 418) scale(0.981 0.975) translate(-601 -418)"/>

    <text class="dist-text"><textPath href="#dist-arc" startOffset="50%" text-anchor="middle">DIST. BY/PAR: THE CINDERMOOR LARDER, QUILLBY, SC 39724 USA</textPath></text>
  </svg>

  <div class="brand brand-the">THE</div>
  <div class="brand brand-name">CINDERMOOR</div>
  <div class="brand-rule brand-rule-left"></div>
  <div class="brand brand-sub">LARDER</div>
  <div class="brand-rule brand-rule-right"></div>

  <div class="product product-en">BLUEBERRIES</div>
  <div class="product product-fr">BLUETS</div>

  <div class="size size-us">1 US Dry Pint&nbsp; | &nbsp;551 ml</div>
  <div class="size size-fr">1 Chopine Seche</div>
  <div class="divider"></div>
</div>
</body>
</html>
```